Harborlight Behavioral and Community Services

Intellectual Developmental Disabilities, Group Homes, Residential Homes and Substance Abuse Residential facilities

Target Market(s)

Adults 18-59 male and female autism, developmental disabilities and mental health

Industry/Entity Type

Intellectual Development Disabilities, Autism, Applied Behavioral Analysis, Mental Health, Substance Abuse

Coding

Coded - Design and coding required

Number of Pages Required

5+ page

Font styles to use
Serif

Colors
0054AA
0677BA
7BADD7
CADEEF
E8F1F8

Requirements
Should not have
• Not specified

```html
<!DOCTYPE html>
<html lang="en">
<head>
<meta charset="utf-8">
<title>Harborlight Behavioral and Community Services</title>
<link rel="stylesheet" href="https://fonts.googleapis.com/css2?family=Lexend:wght@300;400;500;600;700;800&display=swap">
<style>
:root{
  --blue-deep:#0054AA;
  --blue:#0677BA;
  --blue-mid:#7BADD7;
  --blue-pale:#CADEEF;
  --blue-mist:#E8F1F8;
  --navy:#1B2D4F;
  --ink:#1F2A3A;
  --text:#4A5463;
  --white:#ffffff;
  --star:#F5A623;
}
*{box-sizing:border-box;margin:0;padding:0}
html,body{width:1200px;height:4577px;overflow:hidden}
body{font-family:"Lexend",sans-serif;color:var(--ink);background:var(--white);position:relative}
section,header,footer,.bar{position:relative;width:1200px;overflow:hidden}
.abs{position:absolute}
a{color:inherit;text-decoration:none}

/* top bar */
.topbar{height:30px;background:var(--navy);color:var(--white);font-size:11px}
.topbar .tag{left:142px;top:9px}
.topbar .login{right:142px;top:9px;text-decoration:underline;font-weight:500}
.utility{height:37px;background:#EEF3FA}
.socials{left:142px;top:8px;display:flex;gap:6px}
.socials span{width:22px;height:22px;border:1.5px solid var(--blue);border-radius:50%}
.contact-mini{right:290px;top:11px;font-size:11px;display:flex;gap:22px;color:var(--ink)}
.contact-mini svg{vertical-align:-3px;margin-right:5px}
.search{left:940px;top:0;width:36px;height:37px;background:var(--blue-mid);display:flex;align-items:center;justify-content:center}
.donate{left:987px;top:0;width:71px;height:37px;background:var(--blue-deep);color:var(--white);font-size:12px;display:flex;align-items:center;justify-content:center}
.nav{height:75px;background:var(--white);border-bottom:1px solid #EEF1F5}
.brand{left:142px;top:14px;display:flex;align-items:center;gap:10px}
.brand .mark{width:48px;height:48px;border-radius:50%;background:var(--blue)}
.brand .name{font-size:15px;font-weight:500;color:var(--blue-deep);line-height:1.25;width:200px}
.menu{left:571px;top:30px;display:flex;gap:31px;font-size:12px;color:var(--ink)}
.menu .active{color:var(--blue-deep);border-bottom:1.5px solid var(--blue-deep);padding-bottom:2px}

/* hero */
.hero{height:587px;background:var(--white)}
.hero .band{left:0;top:0;width:1200px;height:540px;background:linear-gradient(90deg,#F1EFEE 0%,#ECE8E6 45%,#E3DEDB 100%)}
.hero .photo{left:560px;top:0;width:640px;height:540px;background:linear-gradient(160deg,#E9E5E1 0%,#D9CFC6 45%,#B9AEA6 75%,#E9E6E3 100%)}
.hero h1{left:142px;top:142px;font-size:33px;font-weight:800;line-height:38px;color:var(--blue-deep);letter-spacing:.3px}
.hero .sub{left:142px;top:258px;font-size:17px;line-height:26px;color:var(--blue-deep);width:420px}
.btn{display:inline-flex;align-items:center;justify-content:center;border-radius:20px;background:var(--blue-deep);color:var(--white);font-size:12px;font-weight:500}
.hero .b1{left:142px;top:338px;width:140px;height:38px}
.hero .b2{left:296px;top:338px;width:112px;height:38px}

/* shared headings */
.eyebrow{width:100%;text-align:center;font-size:14px;color:var(--ink)}
.h2{width:100%;text-align:center;font-size:30px;font-weight:500;line-height:44px;color:var(--ink)}
.arrow{width:42px;height:42px;border-radius:50%;border:1.5px solid var(--ink);background:var(--white);display:flex;align-items:center;justify-content:center}

/* services */
.services{height:720px}
.svc-card{top:238px;width:283px;height:390px;background:var(--white);border-radius:8px;box-shadow:0 6px 22px rgba(20,40,80,.10);overflow:hidden}
.svc-card .img{height:210px}
.svc-card .rule{margin:30px 24px 0;border-top:1.5px solid #C9CED6}
.svc-card h3{margin:14px 24px 0;font-size:14px;font-weight:500}
.svc-card p{margin:10px 24px 0;font-size:12px;line-height:22px;color:var(--text)}
.services .more{left:519px;top:674px;width:162px;height:38px}

/* about */
.about{height:645px}
.about .img{left:142px;top:89px;width:439px;height:434px;border-radius:10px;background:linear-gradient(135deg,#E5DED3 0%,#C9B9A6 40%,#8F8072 70%,#D8CFC4 100%)}
.badge{left:350px;top:485px;width:164px;height:75px;background:var(--white);border-radius:8px;box-shadow:0 6px 20px rgba(20,40,80,.12);text-align:center}
.badge b{display:block;font-size:29px;font-weight:600;color:var(--blue-deep);margin-top:10px;line-height:32px}
.badge span{font-size:13px}
.about .label{left:626px;top:99px;font-size:14px}
.about h2{left:626px;top:124px;width:480px;font-size:30px;font-weight:500;line-height:44px}
.about .copy{left:626px;top:230px;width:438px;font-size:12px;line-height:22px;color:var(--text)}
.about .copy p+p{margin-top:10px}
.about .explore{left:626px;top:478px;width:144px;height:38px}

/* how it works */
.how{height:502px;background:var(--blue-mist)}
.how .eyebrow{top:89px;position:absolute}
.how .h2{top:112px;position:absolute}
.step{top:191px;width:192px;height:225px;background:var(--white);border-radius:6px;padding:20px 20px}
.step .ico{width:50px;height:50px;border-radius:50%;background:var(--blue-mist);display:flex;align-items:center;justify-content:center}
.step h3{font-size:14px;font-weight:500;margin-top:20px}
.step p{font-size:11.5px;line-height:20px;margin-top:10px;color:var(--text)}
.step.on{background:var(--blue);color:var(--white)}
.step.on p{color:var(--white)}
.step.on .ico{background:var(--white)}
.how .pic{left:779px;top:191px;width:279px;height:225px;border:1.5px solid var(--blue);border-radius:6px;background:linear-gradient(160deg,#F4F5F6 0%,#E6E7E8 55%,#C9CBCE 100%)}

/* cta */
.cta{height:234px;background:linear-gradient(100deg,#0A4FA3 0%,#0054AA 50%,#0B5CB5 100%);color:var(--white)}
.cta h2{left:142px;top:64px;font-size:32px;font-weight:500}
.cta p{left:142px;top:122px;width:470px;font-size:17px;line-height:29px}
.cta .book{left:868px;top:99px;width:190px;height:38px;background:var(--white);color:var(--ink);font-weight:500}

/* testimonials */
.testi{height:601px}
.testi .eyebrow{top:89px;position:absolute}
.testi .h2{top:114px;position:absolute}
.quote{top:251px;width:438px;height:173px;border:1.5px solid #C9CED6;border-radius:12px;padding:28px 30px}
.quote .qm{position:absolute;top:-38px;left:56px;font-size:60px;font-weight:700;color:var(--blue-mid);background:var(--white);padding:0 6px;line-height:60px}
.quote .row{display:flex;justify-content:space-between;align-items:center}
.quote h4{font-size:14px;font-weight:500;color:var(--blue)}
.stars{color:var(--star);font-size:13px;letter-spacing:2px}
.quote p{margin-top:16px;font-size:11.5px;line-height:22px;color:var(--text)}
.author{top:453px;display:flex;gap:14px;align-items:center}
.author .av{width:44px;height:44px;border-radius:50%;background:linear-gradient(135deg,#C9CED6,#8E98A6)}
.author b{display:block;font-size:14px;font-weight:500}
.author span{font-size:11px;color:var(--text)}
.dots{left:566px;top:514px;display:flex;gap:8px}
.dots i{width:7px;height:7px;border-radius:50%;background:var(--blue-pale)}
.dots i.on{background:var(--blue)}

/* programs */
.programs{height:729px;background:var(--blue-mist)}
.programs .eyebrow{top:91px;position:absolute}
.programs .h2{top:114px;position:absolute}
.grid{left:142px;top:240px;width:916px;height:330px;display:grid;grid-template-columns:repeat(4,1fr);grid-template-rows:165px 165px;border-radius:8px;overflow:hidden;background:var(--white)}
.grid .tx{padding:34px 26px 0}
.grid h3{font-size:14px;font-weight:500;color:var(--blue-deep);line-height:25px}
.grid p{font-size:11.5px;line-height:21px;color:var(--text);margin-top:10px}
.programs .learn{left:471px;top:607px;width:258px;height:39px}

/* footer */
footer{height:417px;background:var(--navy);color:var(--white)}
.fbrand{left:142px;top:86px;width:190px;text-align:center}
.fbrand .mark{width:56px;height:56px;border-radius:50%;border:3px solid var(--white);margin:0 auto}
.fbrand .nm{font-size:26px;font-weight:500;margin-top:20px}
.fbrand .tg{font-size:12px;line-height:22px;margin-top:6px}
.fsocial{left:142px;top:274px;display:flex;gap:19px}
.fsocial span{width:34px;height:34px;border:1.5px solid var(--white);border-radius:50%}
footer h5{font-size:15px;font-weight:500}
footer h5::after{content:"";display:block;width:24px;height:2px;background:var(--blue-mid);margin-top:8px}
.links{left:396px;top:93px}
.links ul{list-style:none;margin-top:16px;font-size:12px;line-height:29px}
.fcontact{left:567px;top:93px;width:270px}
.fcontact .it{position:absolute;left:0;display:flex;gap:16px;font-size:12px;line-height:22px;align-items:center}
.fcontact .ci{width:30px;height:30px;border-radius:50%;background:rgba(255,255,255,.14);display:flex;align-items:center;justify-content:center;flex:none}
.news{left:860px;top:90px;width:199px}
.news p{font-size:12px;line-height:20px;margin-top:16px}
.news .in{margin-top:18px;height:37px;border-radius:20px;background:var(--white);color:#9AA3AF;font-size:11px;padding:11px 20px}
.news .sub{margin-top:18px;width:199px;height:36px;background:var(--blue);font-size:13px}
.fline{left:142px;top:357px;width:916px;border-top:1px solid rgba(255,255,255,.25)}
.copy-l{left:142px;top:381px;font-size:11px}
.copy-r{right:142px;top:381px;font-size:11px}
</style>
</head>
<body>

<div class="bar topbar">
  <span class="abs tag">Transforming Challenges into Strengths: Support, Care, and Growth for Every Journey</span>
  <a class="abs login">Patient Login</a>
</div>

<div class="bar utility">
  <div class="abs socials"><span></span><span></span><span></span><span></span></div>
  <div class="abs contact-mini">
    <span><svg width="13" height="13" viewBox="0 0 24 24" fill="none" stroke="#0054AA" stroke-width="2"><path d="M5 3h4l2 5-3 2a11 11 0 0 0 6 6l2-3 5 2v4a2 2 0 0 1-2 2A17 17 0 0 1 3 5a2 2 0 0 1 2-2z"/></svg>(+00) 555 014 2290</span>
    <span><svg width="15" height="12" viewBox="0 0 24 18" fill="#0054AA"><rect x="1" y="1" width="22" height="16" rx="2"/><path d="M2 2l10 8 10-8" stroke="#fff" stroke-width="2" fill="none"/></svg>info@harborlightcare.org</span>
  </div>
  <div class="abs search"><svg width="15" height="15" viewBox="0 0 24 24" fill="none" stroke="#fff" stroke-width="2.5"><circle cx="10" cy="10" r="7"/><path d="M15 15l6 6"/></svg></div>
  <a class="abs donate">Donate</a>
</div>

<header class="nav">
  <div class="abs brand"><span class="mark"></span><span class="name">Harborlight Behavioral and Community Services</span></div>
  <nav class="abs menu">
    <a class="active">Home</a><a>About Us</a><a>Services</a><a>Resources</a><a>Events</a><a>Blog</a><a>Contact Us</a>
  </nav>
</header>

<section class="hero">
  <div class="abs band"></div>
  <div class="abs photo" role="img" aria-label="Caregiver comforting a distressed young woman seated in a bright room"></div>
  <h1 class="abs">EMPOWERING<br>LIVES THROUGH<br>COMPASSIONATE CARE</h1>
  <p class="abs sub">Specialized Programs for Autism, Developmental Disabilities, and Mental Health</p>
  <a class="abs btn b1">Contact Us Today</a>
  <a class="abs btn b2">Donate Now</a>
</section>

<section class="services">
  <p class="abs eyebrow" style="top:80px">Our Services</p>
  <h2 class="abs h2" style="top:106px">Specialized Care &amp; Tailored Support to Empower<br>Individuals &amp; Foster Independence</h2>
  <div class="abs arrow" style="left:48px;top:413px"><svg width="18" height="12" viewBox="0 0 18 12" fill="none" stroke="#1F2A3A" stroke-width="1.6"><path d="M17 6H1M6 1L1 6l5 5"/></svg></div>
  <div class="abs arrow" style="left:1110px;top:413px"><svg width="18" height="12" viewBox="0 0 18 12" fill="none" stroke="#1F2A3A" stroke-width="1.6"><path d="M1 6h16M12 1l5 5-5 5"/></svg></div>
  <article class="abs svc-card" style="left:142px">
    <div class="img" role="img" aria-label="Mother and young daughter playing with wooden blocks" style="background:linear-gradient(135deg,#E8E2DA,#C7B6A3 60%,#EDE8E2)"></div>
    <div class="rule"></div>
    <h3>Children &amp; Family Service</h3>
    <p>We help foster a supportive, healthy environment in the home for children and families struggling to manage behavioral health needs.</p>
  </article>
  <article class="abs svc-card" style="left:459px">
    <div class="img" role="img" aria-label="Caregiver assisting a smiling older man" style="background:linear-gradient(135deg,#D9DCDF,#A9A39C 55%,#E4E6E8)"></div>
    <div class="rule"></div>
    <h3>Adult Behavioral Health Services</h3>
    <p>Assisting people struggling with mental health or addiction with therapeutic programs and personalized support.</p>
  </article>
  <article class="abs svc-card" style="left:775px">
    <div class="img" role="img" aria-label="Family walking hand in hand through a green park" style="background:linear-gradient(135deg,#B9CFA7,#7FA06A 55%,#C8D8BC)"></div>
    <div class="rule"></div>
    <h3>Foster Care Services</h3>
    <p>Finding safe, loving homes for children and helping them achieve their fullest potential.</p>
  </article>
  <a class="abs btn more">View All Services</a>
</section>

<section class="about">
  <div class="abs img" role="img" aria-label="Support group seated in a circle during a session"></div>
  <div class="abs badge"><b>26K</b><span>Patient Helped</span></div>
  <p class="abs label">About Us</p>
  <h2 class="abs">Dedicated to Empowering Lives<br>&amp; Fostering Independence</h2>
  <div class="abs copy">
    <p>We are committed to providing compassionate, person-centered care for adults with autism, developmental disabilities, and mental health challenges. Our programs are designed to empower individuals, helping them reach their fullest potential and live more independent lives.<br>&nbsp;With a team of experienced professionals, we deliver specialized support tailored to each person's unique needs, ensuring holistic growth.</p>
    <p>We believe in the power of community, promoting inclusion and personal development. Our services are driven by a passion for helping individuals overcome obstacles and embrace their strengths. Together, we build brighter futures.</p>
  </div>
  <a class="abs btn explore">ExploreMore</a>
</section>

<section class="how">
  <p class="eyebrow">How It Work</p>
  <h2 class="h2">Everything You Need We Are For Your Assistance</h2>
  <div class="abs step" style="left:142px">
    <div class="ico"><svg width="22" height="22" viewBox="0 0 24 24" fill="none" stroke="#0677BA" stroke-width="1.6"><circle cx="12" cy="7" r="4"/><path d="M4 21c0-4 4-7 8-7s8 3 8 7"/></svg></div>
    <h3>Consult a Therapist</h3>
    <p>Lorem Ipsum is simply dummy text of the printing and typesetting industry. Lorem Ipsum has been.</p>
  </div>
  <div class="abs step on" style="left:356px">
    <div class="ico"><svg width="22" height="22" viewBox="0 0 24 24" fill="none" stroke="#0677BA" stroke-width="1.6"><rect x="3" y="5" width="18" height="16" rx="2"/><path d="M3 10h18M8 3v4M16 3v4"/></svg></div>
    <h3>Get a Appointments</h3>
    <p>Lorem Ipsum is simply dummy text of the printing and typesetting industry. Lorem Ipsum has been.</p>
  </div>
  <div class="abs step" style="left:567px">
    <div class="ico"><svg width="22" height="22" viewBox="0 0 24 24" fill="none" stroke="#0677BA" stroke-width="1.6"><rect x="3" y="7" width="18" height="13" rx="2"/><path d="M9 7V4h6v3M12 10v7M8.5 13.5h7"/></svg></div>
    <h3>Emergency Case</h3>
    <p>Lorem Ipsum is simply dummy text of the printing and typesetting industry. Lorem Ipsum has been.</p>
  </div>
  <div class="abs pic" role="img" aria-label="Man reading a book in an armchair"></div>
</section>

<section class="cta">
  <h2 class="abs">Ready to Take the Next Step?</h2>
  <p class="abs">Contact us today to learn more about our programs and how we can help.</p>
  <a class="abs btn book">Book Appointment</a>
</section>

<section class="testi">
  <p class="eyebrow">Client Testimonials</p>
  <h2 class="h2">Real Stories, Lasting Impact: Hear from Those We’ve<br>Empowered</h2>
  <div class="abs arrow" style="left:48px;top:317px"><svg width="18" height="12" viewBox="0 0 18 12" fill="none" stroke="#1F2A3A" stroke-width="1.6"><path d="M17 6H1M6 1L1 6l5 5"/></svg></div>
  <div class="abs arrow" style="left:1110px;top:317px"><svg width="18" height="12" viewBox="0 0 18 12" fill="none" stroke="#1F2A3A" stroke-width="1.6"><path d="M1 6h16M12 1l5 5-5 5"/></svg></div>
  <div class="abs quote" style="left:142px">
    <span class="qm">“</span>
    <div class="row"><h4>Consult a Therapist...</h4><span class="stars">★★★★★</span></div>
    <p>“Lorem Ipsum is simply dummy text of the printing and type setting industry. Lorem Ipsum has been the industry's standard dummy text ever since the 1500s.”</p>
  </div>
  <div class="abs quote" style="left:620px">
    <span class="qm">“</span>
    <div class="row"><h4>Consult a Therapist...</h4><span class="stars">★★★★★</span></div>
    <p>“Lorem Ipsum is simply dummy text of the printing and type setting industry. Lorem Ipsum has been the industry's standard dummy text ever since the 1500s.”</p>
  </div>
  <div class="abs author" style="left:216px"><span class="av" role="img" aria-label="Client portrait"></span><div><b>Marcus Ellery</b><span>Lorem Ipsum</span></div></div>
  <div class="abs author" style="left:700px"><span class="av" role="img" aria-label="Client portrait"></span><div><b>Nadia Ferris</b><span>Lorem Ipsum</span></div></div>
  <div class="abs dots"><i class="on"></i><i></i><i></i><i></i><i></i></div>
</section>

<section class="programs">
  <p class="eyebrow">Our Programs</p>
  <h2 class="h2">Comprehensive Programs Designed to Support Growth,<br>Independence, &amp; Community Integration</h2>
  <div class="abs grid">
    <div role="img" aria-label="Stacked books beside a cup of coloured pencils" style="background:linear-gradient(135deg,#EFE6D6,#D8C7A8 60%,#F2ECE2)"></div>
    <div class="tx"><h3>Residential Group<br>Homes</h3><p>Lorem Ipsum is simply dummy text of the printing and.</p></div>
    <div role="img" aria-label="Group of adults talking together indoors" style="background:linear-gradient(135deg,#CFC6BD,#8C7B6E 60%,#DAD2CA)"></div>
    <div class="tx"><h3>Community<br>Integration Programs</h3><p>Lorem Ipsum is simply dummy text of the printing and.</p></div>
    <div class="tx"><h3>Applied Behavioral<br>Analysis (ABA)</h3><p>Lorem Ipsum is simply dummy text of the printing and.</p></div>
    <div role="img" aria-label="Family sitting together on the floor at home" style="background:linear-gradient(135deg,#EDE7DF,#C9B8A5 60%,#F1ECE6)"></div>
    <div class="tx"><h3>Substance Abuse<br>Rehabilitation</h3><p>Lorem Ipsum is simply dummy text of the printing and.</p></div>
    <div role="img" aria-label="Hand arranging wooden cubes with care symbols" style="background:linear-gradient(135deg,#D8B9A3,#A87D62 60%,#E2CBBB)"></div>
  </div>
  <a class="abs btn learn">Learn More About Our Programs</a>
</section>

<footer>
  <div class="abs fbrand">
    <div class="mark"></div>
    <div class="nm">Harborlight</div>
    <div class="tg">Behavioral and Community<br>Services</div>
  </div>
  <div class="abs fsocial"><span></span><span></span><span></span><span></span></div>
  <div class="abs links">
    <h5>Quick Links</h5>
    <ul><li>Home</li><li>Services</li><li>About Us</li><li>Programs</li><li>Resources</li><li>Contact Us</li></ul>
  </div>
  <div class="abs fcontact">
    <h5>Contact Us</h5>
    <div class="it" style="top:52px"><span class="ci"><svg width="12" height="14" viewBox="0 0 24 28" fill="#fff"><path d="M12 0a10 10 0 0 1 10 10c0 8-10 18-10 18S2 18 2 10A10 10 0 0 1 12 0z"/><circle cx="12" cy="10" r="4" fill="#1B2D4F"/></svg></span><span>123, Lorem Ipsum is simply<br>dummy text of the printing and.</span></div>
    <div class="it" style="top:121px"><span class="ci"><svg width="13" height="13" viewBox="0 0 24 24" fill="#fff"><path d="M5 3h4l2 5-3 2a11 11 0 0 0 6 6l2-3 5 2v4a2 2 0 0 1-2 2A17 17 0 0 1 3 5a2 2 0 0 1 2-2z"/></svg></span><span>Phone: (555)-014-2290</span></div>
    <div class="it" style="top:183px"><span class="ci"><svg width="14" height="11" viewBox="0 0 24 18" fill="#fff"><rect x="1" y="1" width="22" height="16" rx="2"/><path d="M2 2l10 8 10-8" stroke="#1B2D4F" stroke-width="2" fill="none"/></svg></span><span>info@harborlightcare.org</span></div>
  </div>
  <div class="abs news">
    <h5>Newsletter</h5>
    <p>Join our subscribers list to get the latest news &amp; special offers.</p>
    <div class="in">Enter your email</div>
    <a class="btn sub">Subscribe Now</a>
  </div>
  <div class="abs fline"></div>
  <p class="abs copy-l">Copyright © 2025 Harborlight Behavioral and Community Services | All Rights Reserved.</p>
  <p class="abs copy-r">Privacy Policy &nbsp;|&nbsp; Terms &amp; Conditions</p>
</footer>

</body>
</html>
```